Clear Plastic Card Design

I am looking to have a business card designed from my logo icon. I am looking to match the style of a different business card I have attached in the files.
Looking for a card that is plastic, with layers of transparency in the shape of my logo icon (also attached in the files) - not a circle like the other card. The winning design will incorporate the red icon logo on the front and back and include the charity's name, "Lanterns for the Weary" in the same or similar font, as well as an email and phone number. For now, use the email: email@lanternsfortheweary.org and the phone number 555-318-4072.
We like how the sample business card has transparency, partial and full opacity layers and a matching color scheme. Files will need to be in vector so that our business card printing company can work with it.
UPDATE:
We've some excellent designs in, thank you everyone! I got an early review from the owner, and he requested a minor redirect to find his perfect design. He wants the design to stand out by NOT being a rectangle. Try instead a circle, square, or best yet - something that falls in the outline of the logo icon, either fully or partially. Thank you, everyone!
Contact Information for Business Card
Lanterns for the Weary text should be incorporated as well as a phone and email.
Look and feel

```html
<!DOCTYPE html>
<html lang="en">
<head>
<meta charset="utf-8">
<title>Lanterns for the Weary – Clear Business Card</title>
<link rel="stylesheet" href="https://fonts.googleapis.com/css2?family=Questrial&family=Open+Sans:wght@400&display=swap">
<style>
  :root {
    --page-bg: #cfc6b9;
    --card-frost: rgba(255, 252, 246, 0.62);
    --card-frost-edge: rgba(238, 228, 214, 0.45);
    --card-rim: rgba(255, 248, 225, 0.9);
    --ink: #141210;
    --red: #c4200c;
    --red-clear: rgba(200, 30, 18, 0.82);
    --orange-clear: rgba(226, 84, 18, 0.55);
    --contact: rgba(244, 232, 226, 0.88);
  }
  * { margin: 0; padding: 0; box-sizing: border-box; }
  html, body {
    width: 1200px;
    height: 926px;
    overflow: hidden;
    background: var(--page-bg);
  }
  .canvas {
    position: relative;
    width: 1200px;
    height: 926px;
  }
  .card {
    position: absolute;
    left: 50px;
    top: 156px;
    width: 1100px;
    height: 614px;
    overflow: hidden;
    border-radius: 3px;
    border: 1.5px solid var(--card-rim);
    background: linear-gradient(120deg, var(--card-frost-edge) 0%, var(--card-frost) 40%, var(--card-frost-edge) 100%);
    box-shadow: 0 8px 24px rgba(0, 0, 0, 0.12);
  }
  .card-waves {
    position: absolute;
    inset: 0;
    width: 100%;
    height: 100%;
  }
  .brand-mark {
    position: absolute;
    left: 455px;
    top: 52px;
    width: 232px;
    height: 232px;
    background: linear-gradient(135deg, var(--red-clear) 0%, rgba(214, 50, 14, 0.78) 55%, var(--orange-clear) 100%);
  }
  .brand-name {
    position: absolute;
    left: 64px;
    top: 240px;
    font-family: "Questrial", sans-serif;
    font-size: 47px;
    line-height: 52px;
    color: var(--ink);
  }
  .contact {
    position: absolute;
    right: 48px;
    top: 480px;
    text-align: right;
    font-family: "Open Sans", sans-serif;
    font-size: 27px;
    line-height: 38px;
    color: var(--contact);
  }
  .contact-line {
    display: flex;
    justify-content: flex-end;
    align-items: center;
    gap: 10px;
  }
  .contact-icon {
    width: 20px;
    height: 20px;
    fill: var(--contact);
  }
</style>
</head>
<body>
<main class="canvas">
  <section class="card">
    <svg class="card-waves" viewBox="0 0 1100 614" preserveAspectRatio="none" aria-hidden="true">
      <defs>
        <linearGradient id="redBand" x1="0" y1="0" x2="1" y2="0">
          <stop offset="0" stop-color="#9b1508" stop-opacity="0.92"/>
          <stop offset="0.45" stop-color="#c81e0e" stop-opacity="0.85"/>
          <stop offset="0.7" stop-color="#d8420f" stop-opacity="0.85"/>
          <stop offset="1" stop-color="#7e1106" stop-opacity="0.92"/>
        </linearGradient>
      </defs>
      <path class="wave-red" d="M0 520 C 160 560 320 560 520 470 C 720 380 900 290 1100 282 L1100 614 L0 614 Z" fill="url(#redBand)"/>
      <path class="wave-black" d="M0 470 C 160 540 330 540 520 450 C 720 355 900 255 1100 250 L1100 270 C 900 266 740 360 540 458 C 330 560 150 555 0 492 Z" fill="var(--ink)"/>
      <path class="wave-sliver" d="M165 515 C 330 520 470 480 610 415 C 480 490 340 528 165 515 Z" fill="var(--ink)"/>
    </svg>

    <span class="brand-mark"></span>
    <p class="brand-name">Lanterns for the<br>Weary</p>

    <div class="contact">
      <p class="contact-line">555-318-4072
        <svg class="contact-icon" viewBox="0 0 24 24" aria-hidden="true"><path d="M6.6 10.8a15.5 15.5 0 0 0 6.6 6.6l2.2-2.2c.3-.3.7-.4 1-.2 1.1.4 2.3.6 3.6.6.6 0 1 .4 1 1V20c0 .6-.4 1-1 1A17 17 0 0 1 3 4c0-.6.4-1 1-1h3.5c.6 0 1 .4 1 1 0 1.3.2 2.5.6 3.6.1.3 0 .7-.2 1z"/></svg>
      </p>
      <p class="contact-line">email@lanternsfortheweary.org
        <svg class="contact-icon" viewBox="0 0 24 24" aria-hidden="true"><path d="M3 5h18v14H3z M4.5 6.5v.3l7.5 5.4 7.5-5.4v-.3z" fill-rule="evenodd"/></svg>
      </p>
    </div>
  </section>
</main>
</body>
</html>
```